" Temos como propósito desenvolver pessoas e proporcionar saúde transformando vidas e sorrisos. Acreditamos que a educação muda pessoas e essas transformam o mundo. E que a manutenção da saúde bucal é fundamental para a saúde geral e o aumento da auto-estima do indivíduo. Nosso principal serviço são os cursos de ortodontia para dentistas já formados (pós-graduação e cursos livres de ortodontia). Temos alguns outros cursos também para dentistas em outras áreas. "

```html
<!DOCTYPE html>
<html lang="pt-BR">
<head>
<meta charset="utf-8">
<title>Ortivo – Cartão de Visita</title>
<link href="https://fonts.googleapis.com/css2?family=Montserrat:wght@400;500;600;700&display=swap" rel="stylesheet">
<style>
  :root {
    --navy: #2c4a5e;
    --maroon: #7b1f42;
    --paper: #ffffff;
    --ink: #2a2f35;
    --muted: #8a9199;
    --rule: #c8ccd0;
    --backdrop: #e4e4e2;
  }
  * { box-sizing: border-box; margin: 0; padding: 0; }
  html, body { width: 1200px; height: 1200px; overflow: hidden; }
  body {
    background: var(--backdrop);
    font-family: "Montserrat", sans-serif;
    color: var(--ink);
    position: relative;
  }
  .card {
    position: absolute;
    left: 240px;
    width: 720px;
    height: 410px;
    border-radius: 22px;
    background: var(--paper);
    overflow: hidden;
  }
  /* Front */
  .card-front { top: 120px; }
  .card-front .base-band {
    position: absolute; left: 0; right: 0; bottom: 0;
    height: 26px; background: var(--navy);
  }
  .front-brand {
    position: absolute; left: 0; right: 0; top: 112px;
    text-align: center;
  }
  .brand-name {
    font-weight: 700;
    font-size: 104px;
    line-height: 1;
    color: var(--navy);
    letter-spacing: -1px;
  }
  .brand-tagline {
    margin-top: 34px;
    font-weight: 500;
    font-size: 24px;
    letter-spacing: 3px;
    color: var(--maroon);
    text-transform: uppercase;
  }
  /* Back */
  .card-back { top: 640px; }
  .back-shape { position: absolute; inset: 0; }
  .name-marker {
    position: absolute; left: 0; top: 58px;
    width: 50px; height: 50px; background: var(--navy);
  }
  .person {
    position: absolute; left: 78px; top: 58px;
  }
  .person-name {
    font-size: 27px; line-height: 1.1; color: var(--ink);
  }
  .person-name strong { font-weight: 700; }
  .person-role {
    margin-top: 4px; font-size: 18px; color: var(--ink);
  }
  .person-rule {
    position: absolute; left: 78px; top: 130px;
    width: 260px; height: 1.5px; background: var(--rule);
  }
  .contacts {
    position: absolute; left: 68px; top: 150px;
    list-style: none;
  }
  .contact {
    display: flex; align-items: center; gap: 18px;
    min-height: 40px; margin-bottom: 8px;
    font-size: 18px; line-height: 1.15;
  }
  .contact-icon {
    width: 32px; height: 32px; flex: none;
    border-radius: 50%; background: var(--navy);
    display: flex; align-items: center; justify-content: center;
  }
  .contact-icon svg { width: 18px; height: 18px; }
  .legal-note {
    position: absolute; left: 20px; bottom: 14px;
    font-size: 8.5px; color: var(--muted);
  }
  .back-brand {
    position: absolute; right: 36px; bottom: 72px;
    text-align: center; color: #fff;
  }
  .back-brand .brand-name { font-size: 52px; color: #fff; }
  .back-brand .brand-tagline {
    margin-top: 12px; font-size: 11px; letter-spacing: 1.5px; color: #fff;
  }
</style>
</head>
<body>

<section class="card card-front" aria-label="Frente do cartão">
  <div class="front-brand">
    <div class="brand-name">Ortivo</div>
    <div class="brand-tagline">Cuidado que transforma</div>
  </div>
  <div class="base-band"></div>
</section>

<section class="card card-back" aria-label="Verso do cartão">
  <svg class="back-shape" viewBox="0 0 720 410" preserveAspectRatio="none" aria-hidden="true">
    <path d="M398 0 Q520 205 398 410" fill="none" stroke="var(--maroon)" stroke-width="3"/>
    <path d="M418 0 Q540 205 418 410 L720 410 L720 0 Z" fill="var(--maroon)"/>
    <path d="M436 0 Q558 205 436 410 L720 410 L720 0 Z" fill="var(--navy)"/>
  </svg>

  <div class="name-marker"></div>
  <div class="person">
    <div class="person-name"><strong>Nome</strong> Sobrenome</div>
    <div class="person-role">Cargo - Função</div>
  </div>
  <div class="person-rule"></div>

  <ul class="contacts">
    <li class="contact">
      <span class="contact-icon">
        <svg viewBox="0 0 24 24"><path fill="#fff" d="M6.6 10.8a15.1 15.1 0 0 0 6.6 6.6l2.2-2.2c.3-.3.7-.4 1-.2 1.1.4 2.3.6 3.6.6.6 0 1 .4 1 1V20c0 .6-.4 1-1 1A17 17 0 0 1 3 4c0-.6.4-1 1-1h3.5c.6 0 1 .4 1 1 0 1.3.2 2.5.6 3.6.1.3 0 .7-.2 1z"/></svg>
      </span>
      <span>11 9876-5432<br>11 9876-5432</span>
    </li>
    <li class="contact">
      <span class="contact-icon">
        <svg viewBox="0 0 24 24"><rect x="3" y="6" width="18" height="12" rx="1.5" fill="#fff"/><path d="M3.5 6.5 12 13l8.5-6.5" fill="none" stroke="var(--navy)" stroke-width="1.6"/></svg>
      </span>
      <span>email@email.com</span>
    </li>
    <li class="contact">
      <span class="contact-icon">
        <svg viewBox="0 0 24 24" fill="none" stroke="#fff" stroke-width="2.4" stroke-linecap="round"><path d="M10 14a4 4 0 0 0 5.7 0l3-3a4 4 0 0 0-5.7-5.7l-1 1"/><path d="M14 10a4 4 0 0 0-5.7 0l-3 3a4 4 0 0 0 5.7 5.7l1-1"/></svg>
      </span>
      <span>www.site.com</span>
    </li>
    <li class="contact">
      <span class="contact-icon">
        <svg viewBox="0 0 24 24"><path fill="#fff" d="M12 2a7 7 0 0 0-7 7c0 5 7 13 7 13s7-8 7-13a7 7 0 0 0-7-7zm0 9.5A2.5 2.5 0 1 1 12 6.5a2.5 2.5 0 0 1 0 5z"/></svg>
      </span>
      <span>Endereço Completo<br>Bairro - Cidade - Estado - Cep</span>
    </li>
  </ul>

  <p class="legal-note">Resp. Técnico: Dr. Paulo Ramos Lima - CRO 00000 - EPAO 0000</p>

  <div class="back-brand">
    <div class="brand-name">Ortivo</div>
    <div class="brand-tagline">CUIDADO QUE TRANSFORMA</div>
  </div>
</section>

</body>
</html>
```